Anzeigengestaltung für Sanitätshaus mit orthopädischer Werkstatt
Zielgruppe
Wir sind ein Sanitätshaus mit orthopädischer Werkstatt. Unsere Firma versorgt Patienten von 2-100 Jahren mit Medizinprodukten. Diese sind z.B. Bandagen, Orthesen, Prothesen, Kompressionsstrümpfe...aber auch Pflegebetten, Rollstühle, Toilettenstühle für ältere pflegebedürftige Patienten. Für die letzteren Hilfsmittel suchen wir einen möglichst jungen (20-40 Jahre) Außendienst. Dieser sollte vielleicht einen medizinischen Beruf gelernt haben. Ist aber kein Zwang. Auf jeden Fall sollte er handwerklich begabt sein. Es muß ein offener, freundicher Mensch mit positiver Ausstrahlung sein der offen ist für neue Aufgaben! Die Arbeit ist sehr abwechslungsreich. Eine Weiterbildung (Dauer 2 Tage im Schulungszentrum) zum Mediziprodukteberater und zahlreiche weitere Schulungen über Hilfsmittel, werden dem neuen Mitarbeiter als Grundlage zur Ausübung des Berufes zur Verfügung gestellt. Der Mitarbeiter fährt nach der ausgiebigen Einarbeitungszeit selbstständig mit unserem Lieferwagen zu Partienten, Pflegediensten, Krankenhäuser und liefert dort Reha-Hilfsmittel aus oder past Medizinprodukte an.
Aufgabenstellung
Im Anhang lade ich unsere jetzige, selbst verfasste Anzeige mit dem Logo von unserer Firma. Wir möchten unsere 'Stellenanzeige' bei Quasselhof, Blinkpost und Lumatok laden. Um diese Anzeige auf diesen Kanälen schalten zu können, müssen diese quadratisch sein.
Wichtig ist! Der Text zur Anzeige soll nicht verändert werden.
Ich habe noch ein tolles Bild was bei Pixavera gelistet ist für diese Anzeige:
https://bilder.pixavera-beispiel.de/de/search?serie_id=918346071&asset_id=918346071

```html
<!DOCTYPE html>
<html lang="de">
<head>
<meta charset="utf-8">
<title>Stellenanzeige Reha-Außendienst – Sanitätshaus Hollerbach</title>
<link rel="stylesheet" href="https://fonts.googleapis.com/css2?family=Barlow+Condensed:wght@500;600&family=Barlow+Semi+Condensed:wght@300;400;500&family=Open+Sans:wght@400;700&display=swap">
<style>
  :root {
    --brand-red: #cf1739;
    --ink: #333333;
    --ink-soft: #5a5a5a;
    --frame: #8c8c8c;
    --paper: #ffffff;
  }
  * { margin: 0; padding: 0; box-sizing: border-box; }
  html, body { width: 1200px; height: 1200px; overflow: hidden; background: var(--paper); }
  .ad {
    position: relative;
    width: 1200px; height: 1200px;
    font-family: "Barlow Semi Condensed", "Arial Narrow", sans-serif;
    color: var(--ink);
  }
  .ad__frame {
    position: absolute; left: 60px; top: 60px;
    width: 1081px; height: 1081px;
    border: 1.5px solid var(--frame);
  }
  .ad__photo {
    position: absolute; left: 585px; top: 75px;
    width: 545px; height: 470px;
    background:
      radial-gradient(ellipse 45% 40% at 72% 45%, rgba(38,108,150,.55), rgba(38,108,150,0) 70%),
      radial-gradient(ellipse 30% 28% at 30% 50%, rgba(200,200,200,.55), rgba(255,255,255,0) 70%),
      radial-gradient(ellipse 70% 60% at 55% 60%, #eceef0, #ffffff 75%);
  }
  .kicker {
    position: absolute; left: 107px; top: 104px;
    font-family: "Barlow Condensed", sans-serif; font-weight: 600;
    font-size: 38px; color: var(--brand-red); letter-spacing: .2px;
  }
  .job-title {
    position: absolute; left: 106px; top: 160px;
    font-family: "Barlow Condensed", sans-serif; font-weight: 600;
    font-size: 56px; line-height: 60px; color: var(--ink);
  }
  .job-facts {
    position: absolute; left: 107px; top: 303px;
    font-size: 27px; line-height: 37px; font-weight: 300;
  }
  .job-facts strong { font-weight: 500; }
  .apply-badge {
    position: absolute; left: 335px; top: 398px;
    width: 272px; height: 148px;
    background: var(--brand-red); border-radius: 26px;
    transform: rotate(-12deg);
    color: #fff; text-align: center;
    font-family: "Open Sans", sans-serif;
    display: flex; flex-direction: column; justify-content: center;
  }
  .apply-badge__call { font-weight: 700; font-size: 24px; line-height: 30px; }
  .apply-badge__mail { font-weight: 700; font-size: 22px; line-height: 30px; }
  .apply-badge__note { font-weight: 400; font-size: 22px; line-height: 30px; }
  .section-title {
    position: absolute; top: 574px;
    font-family: "Barlow Condensed", sans-serif; font-weight: 600;
    font-size: 38px; color: var(--brand-red);
  }
  .section-title--profile { left: 107px; }
  .section-title--offer { left: 628px; }
  .profile-text {
    position: absolute; left: 107px; top: 628px; width: 470px;
    font-size: 27px; line-height: 37px; font-weight: 300;
  }
  .profile-text p + p { margin-top: 14px; }
  .offer-list {
    position: absolute; left: 628px; top: 628px; width: 470px;
    list-style: none;
    font-size: 27px; line-height: 37px; font-weight: 300;
  }
  .offer-list li { position: relative; padding-left: 13px; }
  .offer-list li + li { margin-top: 13px; }
  .offer-list li::before {
    content: ""; position: absolute; left: 1px; top: 18px;
    width: 4px; height: 4px; background: var(--ink);
  }
  .company-name {
    position: absolute; left: 100px; top: 982px; width: 340px;
    font-family: "Barlow Condensed", sans-serif; font-weight: 600;
    font-size: 52px; line-height: 56px; color: var(--brand-red);
  }
  .company-about {
    position: absolute; left: 474px; top: 980px; width: 650px;
    font-size: 20px; line-height: 32px; font-weight: 300; color: var(--ink-soft);
  }
</style>
</head>
<body>
<main class="ad">
  <div class="ad__frame"></div>

  <div class="ad__photo" role="img" aria-label="Foto: junge Mitarbeiterin kniet vor einer lächelnden älteren Dame im Rollstuhl und passt die Fußstütze an"></div>

  <p class="kicker">WIR SUCHEN</p>
  <h1 class="job-title">Reha-Außendienst /<br>Medizinprodukteberater</h1>
  <p class="job-facts">
    <strong>Arbeitsort</strong>: Thum/Erzgebirge<br>
    <strong>Einstellungstermin</strong>: nächstmöglich
  </p>

  <div class="apply-badge">
    <span class="apply-badge__call">ÜBERZEUGEN SIE UNS!</span>
    <span class="apply-badge__mail">info@sanitaet-beispiel.de</span>
    <span class="apply-badge__note">(nur als PDF)</span>
  </div>

  <h2 class="section-title section-title--profile">IHR PROFIL</h2>
  <div class="profile-text">
    <p>Sie sind zwischen 20 und 40 Jahre alt? Haben schon Erfahrung in einem medizinischen Beruf gesammelt und sind handwerklich geschickt?</p>
    <p>Wenn Sie zudem auch noch zuverlässig und zielstrebig sind, freundlich und offen für neue Aufgaben, dann sollten wir uns unbedingt kennenlernen!</p>
  </div>

  <h2 class="section-title section-title--offer">WIR BIETEN</h2>
  <ul class="offer-list">
    <li>eine abwechslungsreiche Arbeit</li>
    <li>eine Weiterbildung (2 Tage) im Schulungszentrum zum Medizinprodukteberater und fortlaufende Qualifikationen</li>
    <li>einen Lieferwagen (nach Einarbeitung) um Reha-Hilfsmittel auszuliefern oder Medizinprodukte anzupassen</li>
  </ul>

  <p class="company-name">Sanitätshaus Hollerbach</p>
  <p class="company-about">Unser Familienunternehmen „Sanitätshaus &amp; orthopädische Werkstatt Hollerbach“ versorgt Menschen mit medizinischen Hilfsmitteln und Produkten für Gesundheit und Wohlbefinden. Wir bieten zukunftssichere und abwechslungsreiche Tätigkeiten mit hervorragenden Perspektiven im Gesundheitswesen.</p>
</main>
</body>
</html>
```